Spectacular Business Card Design for AI SAAS Plattform called Pathleap.ai

Hi Creators
I need an outstanding new Design for my business card.
I run an AI automated Saas Plattform Called Pathleap.ai

Front side:
Logo
Slogan: DIY Business Development & Social Media Management
Data:
Name: Markus Velbringer - CEO / Founder
email: m.velbringer@pathleap-example.ai
mobile: +43 699 82 37 915

Company name:
Pathleap FlexCo

Backside:

What we stand for Slogan:
Vertrauen in KI-Technologie, getragen von menschlicher Vision: Dein Sprung nach vorn!
+ a fancy design what captures our core competencies - AI automisations, Social Media Management, Business development
(dont know if its too much, but AI and social media should be )

pls find attached the logo and the old design

Industry/Entity Type

AI automations for marketing and business development

Contact Information for Business Card

Front side: Logo Slogan: DIY Business Development & Social Media Management Data: Name: Markus Velbringer - CEO / Founder email: m.velbringer@pathleap-example.ai mobile: +43 699 82 37 915 Company name: Pathleap FlexCo Backside: What we stand for Slogan: Vertrauen in KI-Technologie, getragen von menschlicher Vision: Dein Sprung nach vorn!

Font styles to use
Serif
Sans Serif

Requirements
Nice to have
• a fancy design on the backside, a fancy design what captures our core competencies - AI automisations, Social Media Management, Business development

```html
<!DOCTYPE html>
<html lang="de">
<head>
<meta charset="utf-8">
<title>Pathleap.ai – Visitenkarte</title>
<link href="https://fonts.googleapis.com/css2?family=Montserrat:wght@400;500;600;700&family=Open+Sans:wght@400;600&display=swap" rel="stylesheet">
<style>
  :root{
    --teal:#1a8aa6;
    --teal-dark:#136f88;
    --teal-light:#4fb6cf;
    --orange:#f08a2c;
    --ink:#444b50;
    --white:#ffffff;
    --stage:#222426;
  }
  *{box-sizing:border-box;margin:0;padding:0}
  html,body{width:1200px;height:801px;overflow:hidden;background:var(--stage)}
  .stage{position:relative;width:1200px;height:801px}
  .card{
    position:absolute;width:540px;height:309px;border-radius:20px;overflow:hidden;
    box-shadow:0 5px 0 var(--orange),0 14px 30px rgba(0,0,0,.45);
  }
  /* front */
  .card--front{left:36px;top:246px;background:var(--white)}
  .wordmark{
    position:absolute;display:flex;align-items:center;gap:12px;
    font-family:"Montserrat",sans-serif;font-weight:600;letter-spacing:.5px;white-space:nowrap;
  }
  .wordmark__dot{width:18px;height:18px;background:var(--orange)}
  .card--front .wordmark{left:40px;top:48px;font-size:52px;color:var(--teal)}
  .person{position:absolute;left:40px;top:170px;font-family:"Montserrat",sans-serif;white-space:nowrap}
  .person__name{font-size:24px;font-weight:700;color:var(--teal);line-height:1.15}
  .person__role{font-size:16px;font-weight:400;color:var(--ink);margin-top:2px}
  .divider{position:absolute;left:292px;top:152px;width:1px;height:78px;background:var(--teal)}
  .contact{position:absolute;left:306px;top:152px;list-style:none;font-family:"Open Sans",sans-serif;font-size:12px;color:var(--ink);white-space:nowrap}
  .contact li{display:flex;align-items:center;gap:8px;height:26px}
  .contact svg{width:13px;height:13px;flex:none}
  .band{position:absolute;left:0;bottom:0;width:540px;height:80px}
  .band__text{
    position:absolute;right:20px;bottom:11px;font-family:"Montserrat",sans-serif;
    font-size:13px;font-weight:500;color:var(--white);letter-spacing:.2px;white-space:nowrap;
  }
  /* back */
  .card--back{left:624px;top:246px}
  .card__visual{position:absolute;inset:0;background:
    radial-gradient(circle at 55% 38%,rgba(120,210,230,.55),transparent 55%),
    linear-gradient(135deg,#2f9fbf 0%,#1b86a6 55%,#167792 100%)}
  .card--back .wordmark{left:0;right:0;top:96px;justify-content:center;font-size:48px;color:var(--white)}
  .claim{
    position:absolute;left:0;right:0;top:186px;height:66px;padding-top:10px;
    background:rgba(240,138,44,.72);text-align:center;
    font-family:"Montserrat",sans-serif;font-weight:600;font-size:14.5px;line-height:23px;color:var(--white);
  }
</style>
</head>
<body>
<main class="stage">

  <section class="card card--front" aria-label="Vorderseite">
    <div class="wordmark"><span class="wordmark__dot"></span><span>Pathleap</span></div>

    <div class="person">
      <p class="person__name">Markus Velbringer</p>
      <p class="person__role">CEO / Founder</p>
    </div>

    <span class="divider"></span>

    <ul class="contact">
      <li>
        <svg viewBox="0 0 16 16"><path fill="#f08a2c" d="M3 1l3 3-1.5 2a9 9 0 0 0 5.5 5.5L12 10l3 3-2 2C7 15 1 9 1 3z"/></svg>
        +43 699 82 37 915
      </li>
      <li>
        <svg viewBox="0 0 16 16"><rect x="1" y="3" width="14" height="10" rx="1" fill="#f08a2c"/><path d="M1.5 4l6.5 5 6.5-5" fill="none" stroke="#fff" stroke-width="1.3"/></svg>
        m.velbringer@pathleap-example.ai
      </li>
      <li>
        <svg viewBox="0 0 16 16"><circle cx="8" cy="8" r="7" fill="#f08a2c"/><path d="M1 8h14M8 1c-3 3-3 11 0 14M8 1c3 3 3 11 0 14" fill="none" stroke="#fff" stroke-width="1"/></svg>
        www.Pathleap.ai
      </li>
    </ul>

    <svg class="band" viewBox="0 0 540 80" preserveAspectRatio="none" aria-hidden="true">
      <path d="M100 80 C100 58 110 44 138 42 L540 42 L540 80 Z" fill="var(--teal)"/>
    </svg>
    <p class="band__text">DIY Business Development &amp; Social Media Management</p>
  </section>

  <section class="card card--back" aria-label="Rückseite">
    <div class="card__visual" role="img" aria-label="Foto: offene Hände halten ein leuchtendes Netzwerk mit Symbolen sozialer Medien"></div>
    <div class="wordmark"><span class="wordmark__dot"></span><span>Pathleap</span></div>
    <p class="claim">Vertrauen in KI-Technologie, getragen von menschlicher Vision:<br>Dein Sprung nach vorn!</p>
  </section>

</main>
</body>
</html>
```